We have a company that provide sandblasted stone products. Example: numbers for houses. Also we sell cultured stone,brick natural stone to the contractor,homeowner. We need to get a business card that describe our product and service. In the original idea we had an old fashion chisel striking through the x in quelvadine.
Updates

Reason: We realized that 2 days was not enough time for the competion to be open many of the designers may be to busy and require more time to compete.

Industry/Entity Type

It Company

Logo Text

Quelvadine

```html
<!DOCTYPE html>
<html lang="en">
<head>
<meta charset="utf-8">
<title>Quelvadine Business Card</title>
<link href="https://fonts.googleapis.com/css2?family=Arimo:wght@400;700&family=Tinos&display=swap" rel="stylesheet">
<style>
  :root {
    --backdrop: #e4ded5;
    --card: #ffffff;
    --orange: #ee6a22;
    --ink: #2b2b2b;
    --ink-soft: #4a4a4a;
  }
  * { margin: 0; padding: 0; box-sizing: border-box; }
  html, body {
    width: 1200px;
    height: 900px;
    overflow: hidden;
    background: var(--backdrop);
  }
  .canvas {
    position: relative;
    width: 1200px;
    height: 900px;
  }
  .card {
    position: absolute;
    width: 560px;
    height: 320px;
    background: var(--card);
    overflow: hidden;
    box-shadow: 0 10px 28px rgba(0,0,0,0.18);
  }
  .card--contact { left: 150px; top: 110px; }
  .card--brand { left: 490px; top: 470px; }

  .card__shape {
    position: absolute;
    inset: 0;
    width: 100%;
    height: 100%;
  }
  .contact {
    position: absolute;
    left: 34px;
    top: 34px;
    font-family: "Arimo", Arial, sans-serif;
    color: var(--ink-soft);
    font-size: 14px;
    line-height: 1.25;
  }
  .contact__name {
    font-weight: 700;
    font-size: 20px;
    color: var(--ink);
  }
  .contact__role {
    font-size: 14px;
    margin-bottom: 12px;
  }
  .brand {
    position: absolute;
    left: 0;
    right: 0;
    top: 118px;
    display: flex;
    justify-content: center;
    align-items: center;
    gap: 14px;
  }
  .brand__dot {
    width: 22px;
    height: 22px;
    border-radius: 50%;
    background: var(--orange);
  }
  .brand__name {
    font-family: "Tinos", "Times New Roman", serif;
    font-size: 44px;
    letter-spacing: 1px;
    color: var(--ink);
  }
</style>
</head>
<body>
<main class="canvas">

  <section class="card card--contact" aria-label="Card back with contact details">
    <svg class="card__shape" viewBox="0 0 560 320" preserveAspectRatio="none" aria-hidden="true">
      <rect width="560" height="320" fill="var(--orange)"/>
      <path d="M0 0 H255 C330 70 375 190 370 320 H0 Z" fill="var(--card)"/>
    </svg>
    <div class="contact">
      <p class="contact__name">Arlen Voss</p>
      <p class="contact__role">Chief Executive Officer</p>
      <p>Unit 9</p>
      <p>48 Ridgeline Road, Canada</p>
      <p>Tel: 5550 182</p>
      <p>Mob: 5550 347</p>
      <p>Email: arlen@quelvadine.com</p>
      <p>www.quelvadine.com</p>
    </div>
  </section>

  <section class="card card--brand" aria-label="Card front with company name">
    <svg class="card__shape" viewBox="0 0 560 320" preserveAspectRatio="none" aria-hidden="true">
      <path d="M92 282 H560 V320 H62 Z" fill="var(--orange)"/>
    </svg>
    <div class="brand">
      <span class="brand__dot"></span>
      <span class="brand__name">QUELVADINE</span>
    </div>
  </section>

</main>
</body>
</html>
```